photowall advertisement

We require a wall featuring our company logo. We would like to avoid the color green, and gold is highly preferred. The design should be similar to the one in the attached photo. The wall will be used for photos and promotional purposes during congresses. Files must be prepared for printing.
dimension of wall: 470x223 cm

Industry/Entity Type

lifestyle

Colors
0054AA
0677BA
7BADD7
CADEEF
E8F1F8
6B429C
8869AF
B7A5CE
E3DAEB
F3F0F8

Requirements
Must have
• gold color, white, and other compare with gold color
Nice to have
• some pictograms, maps of Europe

```html
<!DOCTYPE html>
<html lang="en">
<head>
<meta charset="utf-8">
<title>Alto Nine – Photo Wall</title>
<link rel="stylesheet" href="https://fonts.googleapis.com/css2?family=Michroma&display=swap">
<style>
  :root {
    --stage: #f4f4f4;
    --wall: #ffffff;
    --gold: #b3952f;
    --shadow: rgba(0, 0, 0, 0.16);
  }
  * { margin: 0; padding: 0; box-sizing: border-box; }
  html, body {
    width: 1028px;
    height: 1200px;
    overflow: hidden;
    background: var(--stage);
  }
  .photo-wall {
    position: absolute;
    left: 20px;
    top: 365px;
    width: 988px;
    height: 469px;
    background: var(--wall);
    box-shadow: 0 12px 40px var(--shadow);
    padding-top: 22px;
  }
  .repeat-row {
    display: flex;
    height: 44px;
    align-items: center;
    padding-left: 29px;
  }
  .repeat-row.offset { padding-left: 70px; }
  .brand-mark {
    width: 155px;
    display: flex;
    align-items: center;
    gap: 7px;
    flex: none;
  }
  .brand-square {
    width: 10px;
    height: 10px;
    background: var(--gold);
    flex: none;
  }
  .brand-name {
    font-family: "Michroma", sans-serif;
    font-size: 12.5px;
    letter-spacing: 1px;
    color: var(--gold);
    white-space: nowrap;
  }
</style>
</head>
<body>
<main class="photo-wall">
  <div class="repeat-row">
    <div class="brand-mark"><span class="brand-square"></span><span class="brand-name">ALTO NINE</span></div>
    <div class="brand-mark"><span class="brand-square"></span><span class="brand-name">ALTO NINE</span></div>
    <div class="brand-mark"><span class="brand-square"></span><span class="brand-name">ALTO NINE</span></div>
    <div class="brand-mark"><span class="brand-square"></span><span class="brand-name">ALTO NINE</span></div>
    <div class="brand-mark"><span class="brand-square"></span><span class="brand-name">ALTO NINE</span></div>
    <div class="brand-mark"><span class="brand-square"></span><span class="brand-name">ALTO NINE</span></div>
  </div>
  <div class="repeat-row offset">
    <div class="brand-mark"><span class="brand-square"></span><span class="brand-name">ALTO NINE</span></div>
    <div class="brand-mark"><span class="brand-square"></span><span class="brand-name">ALTO NINE</span></div>
    <div class="brand-mark"><span class="brand-square"></span><span class="brand-name">ALTO NINE</span></div>
    <div class="brand-mark"><span class="brand-square"></span><span class="brand-name">ALTO NINE</span></div>
    <div class="brand-mark"><span class="brand-square"></span><span class="brand-name">ALTO NINE</span></div>
    <div class="brand-mark"><span class="brand-square"></span><span class="brand-name">ALTO NINE</span></div>
  </div>
  <div class="repeat-row">
    <div class="brand-mark"><span class="brand-square"></span><span class="brand-name">ALTO NINE</span></div>
    <div class="brand-mark"><span class="brand-square"></span><span class="brand-name">ALTO NINE</span></div>
    <div class="brand-mark"><span class="brand-square"></span><span class="brand-name">ALTO NINE</span></div>
    <div class="brand-mark"><span class="brand-square"></span><span class="brand-name">ALTO NINE</span></div>
    <div class="brand-mark"><span class="brand-square"></span><span class="brand-name">ALTO NINE</span></div>
    <div class="brand-mark"><span class="brand-square"></span><span class="brand-name">ALTO NINE</span></div>
  </div>
  <div class="repeat-row offset">
    <div class="brand-mark"><span class="brand-square"></span><span class="brand-name">ALTO NINE</span></div>
    <div class="brand-mark"><span class="brand-square"></span><span class="brand-name">ALTO NINE</span></div>
    <div class="brand-mark"><span class="brand-square"></span><span class="brand-name">ALTO NINE</span></div>
    <div class="brand-mark"><span class="brand-square"></span><span class="brand-name">ALTO NINE</span></div>
    <div class="brand-mark"><span class="brand-square"></span><span class="brand-name">ALTO NINE</span></div>
    <div class="brand-mark"><span class="brand-square"></span><span class="brand-name">ALTO NINE</span></div>
  </div>
  <div class="repeat-row">
    <div class="brand-mark"><span class="brand-square"></span><span class="brand-name">ALTO NINE</span></div>
    <div class="brand-mark"><span class="brand-square"></span><span class="brand-name">ALTO NINE</span></div>
    <div class="brand-mark"><span class="brand-square"></span><span class="brand-name">ALTO NINE</span></div>
    <div class="brand-mark"><span class="brand-square"></span><span class="brand-name">ALTO NINE</span></div>
    <div class="brand-mark"><span class="brand-square"></span><span class="brand-name">ALTO NINE</span></div>
    <div class="brand-mark"><span class="brand-square"></span><span class="brand-name">ALTO NINE</span></div>
  </div>
  <div class="repeat-row offset">
    <div class="brand-mark"><span class="brand-square"></span><span class="brand-name">ALTO NINE</span></div>
    <div class="brand-mark"><span class="brand-square"></span><span class="brand-name">ALTO NINE</span></div>
    <div class="brand-mark"><span class="brand-square"></span><span class="brand-name">ALTO NINE</span></div>
    <div class="brand-mark"><span class="brand-square"></span><span class="brand-name">ALTO NINE</span></div>
    <div class="brand-mark"><span class="brand-square"></span><span class="brand-name">ALTO NINE</span></div>
    <div class="brand-mark"><span class="brand-square"></span><span class="brand-name">ALTO NINE</span></div>
  </div>
  <div class="repeat-row">
    <div class="brand-mark"><span class="brand-square"></span><span class="brand-name">ALTO NINE</span></div>
    <div class="brand-mark"><span class="brand-square"></span><span class="brand-name">ALTO NINE</span></div>
    <div class="brand-mark"><span class="brand-square"></span><span class="brand-name">ALTO NINE</span></div>
    <div class="brand-mark"><span class="brand-square"></span><span class="brand-name">ALTO NINE</span></div>
    <div class="brand-mark"><span class="brand-square"></span><span class="brand-name">ALTO NINE</span></div>
    <div class="brand-mark"><span class="brand-square"></span><span class="brand-name">ALTO NINE</span></div>
  </div>
  <div class="repeat-row offset">
    <div class="brand-mark"><span class="brand-square"></span><span class="brand-name">ALTO NINE</span></div>
    <div class="brand-mark"><span class="brand-square"></span><span class="brand-name">ALTO NINE</span></div>
    <div class="brand-mark"><span class="brand-square"></span><span class="brand-name">ALTO NINE</span></div>
    <div class="brand-mark"><span class="brand-square"></span><span class="brand-name">ALTO NINE</span></div>
    <div class="brand-mark"><span class="brand-square"></span><span class="brand-name">ALTO NINE</span></div>
    <div class="brand-mark"><span class="brand-square"></span><span class="brand-name">ALTO NINE</span></div>
  </div>
  <div class="repeat-row">
    <div class="brand-mark"><span class="brand-square"></span><span class="brand-name">ALTO NINE</span></div>
    <div class="brand-mark"><span class="brand-square"></span><span class="brand-name">ALTO NINE</span></div>
    <div class="brand-mark"><span class="brand-square"></span><span class="brand-name">ALTO NINE</span></div>
    <div class="brand-mark"><span class="brand-square"></span><span class="brand-name">ALTO NINE</span></div>
    <div class="brand-mark"><span class="brand-square"></span><span class="brand-name">ALTO NINE</span></div>
    <div class="brand-mark"><span class="brand-square"></span><span class="brand-name">ALTO NINE</span></div>
  </div>
  <div class="repeat-row offset">
    <div class="brand-mark"><span class="brand-square"></span><span class="brand-name">ALTO NINE</span></div>
    <div class="brand-mark"><span class="brand-square"></span><span class="brand-name">ALTO NINE</span></div>
    <div class="brand-mark"><span class="brand-square"></span><span class="brand-name">ALTO NINE</span></div>
    <div class="brand-mark"><span class="brand-square"></span><span class="brand-name">ALTO NINE</span></div>
    <div class="brand-mark"><span class="brand-square"></span><span class="brand-name">ALTO NINE</span></div>
    <div class="brand-mark"><span class="brand-square"></span><span class="brand-name">ALTO NINE</span></div>
  </div>
</main>
</body>
</html>
```